Young, dynamic furniture company needs a new business card design

We require a new business card design for our modern furniture company which supplies furniture and appliances to the property and development market.
Tallowvale Furnishing has become one of the leading furniture & appliance suppliers to the property market withing London. With over 10 years experience, we have increased our business to supply not only private landlords and managing agents, but also property developers, housing associations and local councils.
We offer not only a complete range of furniture which includes beds, wardrobes, dining sets and sofas, but also a high quality, full delivery and assembly service to help you with all our furnishing needs.

Target Market(s)

Private landlords, estate agents, letting agents, property management companies

Industry/Entity Type

Business

Contact Information for Business Card

Name,
Title,
Address,
Mobile,
Telephone,
Fax, Website, email address

Font styles to use
Sans Serif

Colors
3176b5
0555a3
85abd2
cfdeed

Requirements
Must have
• All the above information for each of our staff, along with our logo

```html
<!DOCTYPE html>
<html lang="en">
<head>
<meta charset="utf-8">
<title>Tallowvale Furnishing – Business Card</title>
<link rel="stylesheet" href="https://fonts.googleapis.com/css2?family=Ubuntu:wght@400;500;700&family=Quicksand:wght@500;600&display=swap">
<style>
  :root {
    --blue-deep: #0a78c6;
    --blue-mid: #0a6a9c;
    --teal-green: #03897a;
    --strip-left: #0d82cc;
    --strip-right: #00b3a0;
    --white: #ffffff;
    --ink: #333333;
    --ink-soft: #555555;
    --accent: #139ec2;
    --mark: #3d4d7e;
  }
  * { margin: 0; padding: 0; box-sizing: border-box; }
  html, body { width: 1200px; height: 720px; overflow: hidden; background: #ffffff; }
  .card {
    position: relative;
    width: 1200px;
    height: 720px;
    overflow: hidden;
    background: linear-gradient(90deg, var(--blue-deep) 0%, var(--blue-mid) 50%, var(--teal-green) 100%);
  }
  .top-strip {
    position: absolute;
    left: 0; top: 171px;
    width: 1200px; height: 58px;
    background: linear-gradient(90deg, #0c7cc2 0%, #0b86b6 50%, #049a8c 100%);
    box-shadow: 0 -8px 14px rgba(0,0,0,0.25);
  }
  .info-band {
    position: absolute;
    left: 0; top: 229px;
    width: 1200px; height: 264px;
    background: var(--white);
  }
  .brand {
    position: absolute;
    left: 196px; top: 282px;
    width: 280px;
    display: flex; flex-direction: column; align-items: center;
  }
  .brand-square {
    width: 110px; height: 110px;
    background: var(--mark);
    margin-bottom: 24px;
  }
  .brand-name {
    font-family: "Ubuntu", sans-serif;
    font-weight: 400;
    font-size: 21px;
    text-transform: uppercase;
    color: var(--ink-soft);
    white-space: nowrap;
  }
  .company-name {
    position: absolute;
    left: 503px; top: 262px;
    font-family: "Ubuntu", sans-serif;
    font-weight: 700;
    font-size: 54px;
    letter-spacing: -2px;
    color: var(--ink);
    white-space: nowrap;
  }
  .company-name .lead { color: var(--accent); }
  .contact-list {
    position: absolute;
    left: 512px; top: 327px;
    list-style: none;
  }
  .contact-item {
    display: flex; align-items: center;
    height: 32px;
    font-family: "Quicksand", sans-serif;
    font-weight: 500;
    font-size: 24px;
    color: var(--ink);
  }
  .contact-tag {
    position: relative;
    width: 19px; height: 19px;
    margin-right: 10px;
    border-radius: 3px;
    background: var(--ink);
    color: var(--white);
    font-family: "Ubuntu", sans-serif;
    font-weight: 500;
    font-size: 13px;
    line-height: 19px;
    text-align: center;
  }
  .contact-tag::after {
    content: "";
    position: absolute;
    right: -5px; top: 6px;
    border-left: 5px solid var(--ink);
    border-top: 4px solid transparent;
    border-bottom: 4px solid transparent;
  }
  .social-band {
    position: absolute;
    left: 40px; top: 493px;
    width: 1160px; height: 59px;
    background: linear-gradient(90deg, var(--strip-left) 0%, #0a9cc8 50%, var(--strip-right) 100%);
    box-shadow: 0 6px 10px rgba(0,0,0,0.25);
  }
  .social-link {
    position: absolute;
    top: 0; height: 59px;
    display: flex; align-items: center;
    font-family: "Quicksand", sans-serif;
    font-weight: 500;
    font-size: 24px;
    color: var(--white);
  }
  .social-dot {
    width: 29px; height: 29px;
    border-radius: 50%;
    background: var(--white);
    margin-right: 12px;
  }
  .crop-mark { position: absolute; background: #222222; }
  .crop-mark.v { width: 1px; height: 17px; }
  .crop-mark.h { width: 17px; height: 1px; }
</style>
</head>
<body>
  <div class="card">
    <div class="top-strip"></div>

    <section class="info-band"></section>

    <div class="brand">
      <div class="brand-square"></div>
      <div class="brand-name">Tallowvale Furnishing</div>
    </div>

    <h1 class="company-name"><span class="lead">Company</span> Name</h1>

    <ul class="contact-list">
      <li class="contact-item"><span class="contact-tag">A</span>business address</li>
      <li class="contact-item"><span class="contact-tag">T</span>012 . 345 . 6789</li>
      <li class="contact-item"><span class="contact-tag">E</span>name@email.com</li>
      <li class="contact-item"><span class="contact-tag">W</span>website.com</li>
    </ul>

    <nav class="social-band">
      <span class="social-link" style="left:266px"><span class="social-dot"></span>friendpage</span>
      <span class="social-link" style="left:519px"><span class="social-dot"></span>chirpnet</span>
      <span class="social-link" style="left:734px"><span class="social-dot"></span>searchly</span>
    </nav>

    <span class="crop-mark v" style="left:40px; top:0"></span>
    <span class="crop-mark h" style="left:0; top:40px"></span>
    <span class="crop-mark v" style="left:1160px; top:0"></span>
    <span class="crop-mark h" style="left:1183px; top:40px"></span>
    <span class="crop-mark v" style="left:40px; top:703px"></span>
    <span class="crop-mark h" style="left:0; top:679px"></span>
    <span class="crop-mark v" style="left:1160px; top:703px"></span>
    <span class="crop-mark h" style="left:1183px; top:679px"></span>
  </div>
</body>
</html>
```